Business Sign

I need a business sign designed, based on the business card design/logo/font/colours I have previously had created by Artnest. It is to be a window decal which will be affixed to the inside of my business window front. I will probably have it printed through Pressloom. The largest size available through PressLoom is 49 x 32.1cm therefore I would like a series of three signs that will be positioned down the front of my window.
Information I require on sign 1 includes:
business name and logo
phone number
web address
email address
Information I require on sign 2 includes:
Sewing Classes Beginner to Advanced
Social Sewing Classes
Pattern Fitting Classes
Pattern Drafting Classes
Information I require on sign 3 includes:
Alteration Services
Dressmaking Services
Auxiliary Services
As a suggestion, please view my website homepage on www.threadmeadow.com.au as the background dressmaking themed cliparts may provide some inspiration to "decorate" the signs.

Target Market(s)

For sewing classes:
predominately female, 18-65yo, stay-at-home mums, professional women seeking creative outlet, women wanting to sell on-line or at markets, young adults looking to enter the fashion industry, retired women sewing as a hobby, women with fitting issues who find it difficult to find clothes in shops
For alterations:
all age groups male and female

Industry/Entity Type

Business

Font styles to use
Other font styles liked:
• as per business card

Requirements
Must have
• must be similar to business card in style, font, colour, look etc......

```html
<!DOCTYPE html>
<html lang="en">
<head>
<meta charset="utf-8">
<title>Thread Meadow – Window Signs</title>
<link rel="stylesheet" href="https://fonts.googleapis.com/css2?family=Oswald:wght@400;500&family=Caveat:wght@500&display=swap">
<style>
  :root {
    --page: #fcf0fd;
    --card: #fdf4f6;
    --card-edge: #f9e6ee;
    --plum: #4f3c4b;
    --pink: #f08cbb;
    --pink-soft: #f5a9cb;
    --lilac: #dcbfd9;
    --blush: #f7d6e6;
    --white: #ffffff;
  }
  * { margin: 0; padding: 0; box-sizing: border-box; }
  html, body { width: 1200px; height: 1000px; overflow: hidden; }
  body { background: var(--page); position: relative; font-family: "Oswald", "Arial Narrow", sans-serif; }

  .sign {
    position: absolute; width: 442px; height: 286px; overflow: hidden;
    background: linear-gradient(135deg, var(--white) 0%, var(--card) 55%, var(--card-edge) 100%);
    box-shadow: 0 3px 12px rgba(60, 40, 60, 0.55);
  }
  .sign-contact { left: 88px; top: 48px; }
  .sign-classes { left: 266px; top: 354px; }
  .sign-services { left: 590px; top: 667px; background: linear-gradient(135deg, #fdf3f6 0%, #fbe3ed 100%); }

  .sign svg.swoosh { position: absolute; inset: 0; width: 100%; height: 100%; }

  .mannequin { position: absolute; border-radius: 40% 40% 30% 30% / 20% 20% 12% 12%; }
  .sign-contact .mannequin { left: 36px; top: 20px; width: 80px; height: 258px; background: linear-gradient(180deg, var(--blush), #f1c4db); }
  .sign-classes .mannequin { left: 350px; top: 58px; width: 56px; height: 210px; background: linear-gradient(180deg, var(--lilac), #d6b3d2); }
  .sign-services .mannequin { left: 326px; top: 24px; width: 62px; height: 210px; background: linear-gradient(180deg, var(--blush), #efc0d8); }

  .brand-name {
    position: absolute; left: 132px; top: 42px;
    font-weight: 400; font-size: 40px; color: var(--plum); letter-spacing: 0.5px;
  }
  .contact-list { position: absolute; right: 12px; top: 201px; list-style: none; text-align: right; }
  .contact-list li {
    display: flex; justify-content: flex-end; align-items: center; gap: 6px;
    font-size: 15px; line-height: 26px; color: var(--pink-soft);
  }
  .contact-list svg { width: 15px; height: 15px; }

  .top-band { position: absolute; left: 0; top: 0; width: 100%; height: 20px; background: var(--plum); }
  .tab {
    position: absolute; left: 264px; top: 8px; width: 98px; height: 24px;
    background: var(--plum); border-radius: 0 0 10px 10px;
    color: var(--white); font-size: 12px; text-align: center; line-height: 20px;
  }

  .service-list { position: absolute; list-style: none; }
  .service-list li { font-size: 21px; line-height: 35px; color: var(--pink); white-space: nowrap; }
  .service-list li::before { content: "• "; }
  .sign-classes .service-list { left: 10px; top: 52px; }
  .sign-services .service-list { left: 42px; top: 84px; }

  .tagline {
    position: absolute; right: 10px; bottom: 6px;
    font-family: "Caveat", cursive; font-size: 19px; color: var(--pink);
  }
</style>
</head>
<body>

<section class="sign sign-contact">
  <svg class="swoosh" viewBox="0 0 442 286" aria-hidden="true">
    <path d="M0,282 C140,300 300,240 442,110 L442,286 L0,286 Z" fill="var(--plum)"/>
    <path d="M0,270 C150,296 300,230 442,105 L442,112 C300,246 150,300 0,286 Z" fill="var(--white)"/>
    <path d="M0,222 C140,282 300,230 442,104 C300,250 140,310 0,252 Z" fill="var(--pink)"/>
    <path d="M20,244 C150,270 260,240 340,200 C260,252 140,280 20,250 Z" fill="var(--white)" opacity="0.8"/>
  </svg>
  <div class="mannequin" role="img" aria-label="Dress form illustration in pink with a lilac sash bow"></div>
  <h1 class="brand-name">Thread Meadow</h1>
  <ul class="contact-list">
    <li>0400 555 218
      <svg viewBox="0 0 16 16" aria-hidden="true"><path d="M2,6 C2,3 14,3 14,6 L12,7 L11,5 L5,5 L4,7 Z M4,8 L12,8 L13,13 L3,13 Z" fill="var(--pink-soft)"/></svg>
    </li>
    <li>info@threadmeadow.com.au
      <svg viewBox="0 0 16 16" aria-hidden="true"><rect x="1.5" y="3.5" width="13" height="9" fill="none" stroke="var(--pink-soft)" stroke-width="1.6"/><path d="M1.5,3.5 L8,9 L14.5,3.5" fill="none" stroke="var(--pink-soft)" stroke-width="1.6"/></svg>
    </li>
    <li>www.threadmeadow.com.au
      <svg viewBox="0 0 16 16" aria-hidden="true"><circle cx="8" cy="8" r="6.5" fill="none" stroke="var(--pink-soft)" stroke-width="1.5"/><ellipse cx="8" cy="8" rx="2.8" ry="6.5" fill="none" stroke="var(--pink-soft)" stroke-width="1.2"/><path d="M1.5,8 H14.5" stroke="var(--pink-soft)" stroke-width="1.2"/></svg>
    </li>
  </ul>
</section>

<section class="sign sign-classes">
  <svg class="swoosh" viewBox="0 0 442 286" aria-hidden="true">
    <path d="M0,230 C120,300 280,260 442,120 L442,128 C280,280 110,300 0,262 Z" fill="var(--pink)"/>
    <path d="M20,246 C150,290 260,262 320,232 C250,276 130,290 20,252 Z" fill="var(--white)" opacity="0.8"/>
  </svg>
  <div class="top-band"></div>
  <div class="tab">Thread Meadow</div>
  <ul class="service-list">
    <li>Sewing Classes Beginner to Advanced</li>
    <li>Social Sewing Classes</li>
    <li>Pattern Fitting Classes</li>
    <li>Pattern Drafting Classes</li>
  </ul>
  <div class="mannequin" role="img" aria-label="Lilac dress form on a stand"></div>
</section>

<section class="sign sign-services">
  <svg class="swoosh" viewBox="0 0 442 286" aria-hidden="true">
    <path d="M0,22 C90,2 180,-2 260,0 C170,8 80,30 0,52 Z" fill="var(--plum)"/>
    <path d="M30,18 C120,6 200,2 260,0 C190,10 110,24 40,30 Z" fill="var(--plum)" opacity="0.85"/>
    <path d="M0,212 C120,268 300,220 442,112 L442,124 C300,240 130,290 0,250 Z" fill="var(--plum)"/>
    <path d="M40,228 C150,262 240,250 300,230 C240,258 150,268 40,236 Z" fill="var(--plum)" opacity="0.85"/>
  </svg>
  <ul class="service-list">
    <li>Alteration Services</li>
    <li>Dressmaking Services</li>
    <li>Auxiliary Services</li>
  </ul>
  <div class="mannequin" role="img" aria-label="Pink dress form with a lilac sash bow on a curled stand"></div>
  <p class="tagline">Where Every Stitch Finds Its Shape</p>
</section>

</body>
</html>
```